Banner Ad for a Holding Page of a Website - Power Parcel

We require a sort of banner ad or an impactful image to use in the holding page, while we work on a final worksite, while providing basic information about the project.
In other words, a nice image instead of (or in addition to) using the boring "under construction" text.
The project is a new service, which consists of sending highly trained energy efficiency technicians to homes for a 2 hour intervention in order to help householders improve the energy efficiency of their homes. These interventions consist of adjusting the central thermostat, maybe installing thermostatic valves on the radiators, low consumption lightbulbs, etc. In addition, these technicians will also provide the householders advise for improving the energy efficiency of their homes, e.g. length of showers, more efficient ways of cooking, washing, etc. I'm attaching a couple of ideas (banner 1 & 2) that I like in terms of nice and different images for the holding page banner. Also, feel free to google the following measures we install or adjust: thermostatic radiator valves, room or central thermostats, LED lightbulbs or low consumption light bulbs. Which might trigger some nice ideas for this banner. I'm looking forward to seeing your proposals or let me know if you need further information (I'm attaching also an initial write up about the project).

March 6th:
I've just added a file with the current thinking on the holding page (including a top logo). Please note the red section, which is the specific image briefed to Sketch Plaza designers. The project is not the whole page, it is only the "under construction" image. Thanks

Target Market(s)

Mainly households interested in energy saving, due to high costs of energy, the environment or improving comfort.

Industry/Entity Type

Construction

Colors

Designer to choose colors to be used in the design.

Requirements
Must have
• Convey the idea of under construction or coming soon.
Creativity relevant to the project.

```html
<!DOCTYPE html>
<html lang="en">
<head>
<meta charset="utf-8">
<title>Power Parcel – Coming Soon</title>
<link href="https://fonts.googleapis.com/css2?family=Arimo:wght@400;700&family=Oswald:wght@700&display=swap" rel="stylesheet">
<style>
  :root {
    --green-deep: #0f4f22;
    --green-mid: #1e7a37;
    --green-light: #2f9a4e;
    --ribbon-white: #f4f6f4;
    --ribbon-text: #1d6a31;
    --title-text: #eef2ef;
    --body-text: #e9f1ea;
    --bulb-shade: rgba(10, 55, 22, 0.55);
  }
  html, body {
    margin: 0;
    padding: 0;
    overflow: hidden;
    background: #ffffff;
  }
  .banner {
    position: relative;
    width: 1200px;
    height: 700px;
    overflow: hidden;
    background:
      radial-gradient(ellipse 520px 300px at 560px 330px, rgba(8, 60, 24, 0.55), transparent 70%),
      radial-gradient(ellipse 500px 260px at 120px 650px, rgba(70, 170, 100, 0.45), transparent 70%),
      radial-gradient(ellipse 500px 300px at 1100px 80px, rgba(70, 170, 100, 0.35), transparent 70%),
      linear-gradient(160deg, var(--green-light) 0%, var(--green-mid) 45%, var(--green-deep) 70%, var(--green-mid) 100%);
    font-family: "Arimo", Arial, sans-serif;
  }
  .bulb-decoration {
    position: absolute;
    left: 830px;
    top: 220px;
    width: 300px;
    height: 470px;
    border-radius: 45% 45% 30% 30%;
    background: radial-gradient(ellipse at 50% 45%, var(--bulb-shade), transparent 72%);
    transform: rotate(-28deg);
  }
  .coming-soon {
    position: absolute;
    left: 0;
    top: 0;
  }
  .brand-title {
    position: absolute;
    left: 250px;
    width: 695px;
    top: 92px;
    margin: 0;
    text-align: center;
    font-family: "Arimo", Arial, sans-serif;
    font-weight: 700;
    font-size: 88px;
    line-height: 1;
    letter-spacing: 2px;
    text-transform: uppercase;
    color: var(--title-text);
  }
  .tagline {
    position: absolute;
    left: 0;
    right: 0;
    top: 262px;
    margin: 0;
    padding-left: 4px;
    text-align: center;
    font-size: 42px;
    font-weight: 400;
    letter-spacing: 1.2px;
    color: var(--body-text);
    text-shadow: 1px 2px 3px rgba(0, 0, 0, 0.35);
  }
  .service-list {
    position: absolute;
    left: 214px;
    top: 366px;
    margin: 0;
    padding: 0;
    list-style: none;
    font-size: 29px;
    letter-spacing: 0.6px;
    line-height: 41.6px;
    color: var(--body-text);
    text-shadow: 1px 2px 3px rgba(0, 0, 0, 0.3);
  }
  .service-list li {
    position: relative;
    padding-left: 24px;
  }
  .service-list li::before {
    content: "";
    position: absolute;
    left: 3px;
    top: 18px;
    width: 7px;
    height: 7px;
    border-radius: 50%;
    background: var(--body-text);
  }
</style>
</head>
<body>
  <main class="banner">
    <div class="bulb-decoration" role="img" aria-label="Faint silhouette of a low consumption lightbulb"></div>

    <svg class="coming-soon" width="320" height="320" viewBox="0 0 320 320" aria-label="Coming soon">
      <polygon points="0,198 198,0 300,0 0,300" fill="var(--ribbon-white)"/>
      <text x="0" y="0" transform="translate(124.5 124.5) rotate(-45) translate(0 18)"
            text-anchor="middle" font-family="Oswald, sans-serif" font-weight="700"
            font-size="50" fill="var(--ribbon-text)"
            textLength="290" lengthAdjust="spacingAndGlyphs">COMING SOON</text>
    </svg>

    <h1 class="brand-title">Power Parcel</h1>
    <p class="tagline">Learn to reduce your energy bills today</p>

    <ul class="service-list">
      <li>Highly trained energy efficiency technicians</li>
      <li>2 Hour interventions</li>
      <li>Central thermostat adjustment</li>
      <li>Thermostatic valve installation on radiators</li>
      <li>Low consumption lightbulb installation</li>
      <li>Energy efficiency advice</li>
    </ul>
  </main>
</body>
</html>
```